Eye-catching Card for new church

I would like a card the size of a business card ... that can be used to announce the start of our new church. I would like it to have our logo on the card, my name, and the statement "Coming Soon ... 1.10.2016". I also would like to list our website address and Facebook page and my Twitter account.

Target Market(s)

prospective people looking for a church

Industry/Entity Type

Church

Requirements
Must have
• a focus on Coming Soon ... 1.10.2016
• Brightfold Church logo
Should not have
• church buildings or writings on the cross

```html
<!DOCTYPE html>
<html lang="en">
<head>
<meta charset="utf-8">
<title>Brightfold Church – Coming Soon Card</title>
<link rel="stylesheet" href="https://fonts.googleapis.com/css2?family=Cinzel:wght@400;500&family=Open+Sans:wght@400;600&display=swap">
<style>
  :root {
    --page-bg: #ecebe8;
    --card-white: #ffffff;
    --blue-deep: #1f3fa6;
    --blue-mid: #2a6fc4;
    --blue-light: #3f96d8;
    --swoosh-dark: #2b2b2e;
    --swoosh-light: #b9bbbf;
    --ink: #2a2a2c;
    --text-light: #ffffff;
  }
  html, body {
    margin: 0;
    width: 1200px;
    height: 1000px;
    overflow: hidden;
    background: var(--page-bg);
  }
  .canvas {
    position: relative;
    width: 1200px;
    height: 1000px;
  }
  .card {
    position: absolute;
    left: 100px;
    top: 202px;
    width: 1000px;
    height: 596px;
    border-radius: 36px;
    overflow: hidden;
    background: var(--card-white);
    box-shadow: 0 6px 18px rgba(0,0,0,0.18);
  }
  .card-shapes {
    position: absolute;
    inset: 0;
  }
  .announcement {
    position: absolute;
    top: 26px;
    left: 0;
    width: 100%;
    text-align: center;
    font-family: "Open Sans", sans-serif;
    font-weight: 600;
    font-size: 26px;
    color: var(--text-light);
    margin: 0;
  }
  .brand {
    position: absolute;
    top: 150px;
    left: 0;
    width: 100%;
    text-align: center;
    font-family: "Cinzel", serif;
    font-weight: 400;
    color: var(--ink);
  }
  .brand-mark {
    display: block;
    width: 64px;
    height: 64px;
    margin: 0 auto 22px;
    border-radius: 50%;
    background: var(--blue-mid);
  }
  .brand-name {
    display: block;
    font-size: 54px;
    letter-spacing: 5px;
    line-height: 1;
  }
  .brand-sub {
    display: block;
    font-size: 22px;
    letter-spacing: 12px;
    margin-top: 8px;
  }
  .contact-name {
    position: absolute;
    left: 218px;
    top: 495px;
    margin: 0;
    font-family: "Cinzel", serif;
    font-weight: 400;
    font-size: 32px;
    color: var(--text-light);
  }
  .contact-list {
    position: absolute;
    left: 496px;
    top: 478px;
    margin: 0;
    padding: 0;
    list-style: none;
    font-family: "Open Sans", sans-serif;
    font-size: 25px;
    line-height: 32px;
    color: var(--text-light);
  }
  .contact-list li {
    display: flex;
    align-items: center;
    gap: 8px;
  }
  .contact-icon {
    width: 16px;
    height: 16px;
    flex: none;
  }
  .dot {
    width: 13px;
    height: 13px;
    border-radius: 50%;
    background: var(--text-light);
    margin: 0 1px 0 2px;
    flex: none;
  }
</style>
</head>
<body>
<div class="canvas">
  <article class="card">
    <svg class="card-shapes" width="1000" height="596" viewBox="0 0 1000 596" aria-hidden="true">
      <defs>
        <linearGradient id="bandBlue" x1="0" y1="0" x2="1" y2="0">
          <stop offset="0" stop-color="var(--blue-deep)"/>
          <stop offset="0.5" stop-color="var(--blue-light)"/>
          <stop offset="1" stop-color="var(--blue-deep)"/>
        </linearGradient>
        <linearGradient id="swooshGrey" x1="0" y1="0" x2="1" y2="0">
          <stop offset="0" stop-color="var(--swoosh-light)" stop-opacity="0"/>
          <stop offset="0.35" stop-color="var(--swoosh-dark)"/>
          <stop offset="0.7" stop-color="var(--swoosh-light)"/>
          <stop offset="1" stop-color="var(--swoosh-light)" stop-opacity="0"/>
        </linearGradient>
      </defs>
      <!-- top band -->
      <path class="band-top" d="M0 0 H1000 V20 Q500 125 0 20 Z" fill="url(#bandBlue)"/>
      <path class="swoosh-top" d="M60 25 Q500 120 940 25 Q500 98 60 25 Z" fill="url(#swooshGrey)"/>
      <!-- bottom band -->
      <path class="band-bottom" d="M0 500 Q500 380 1000 500 V596 H0 Z" fill="url(#bandBlue)"/>
      <path class="swoosh-bottom" d="M70 476 Q500 388 930 476 Q500 408 70 476 Z" fill="url(#swooshGrey)"/>
    </svg>

    <p class="announcement">Coming Soon ... 1.10.2015</p>

    <div class="brand">
      <span class="brand-mark"></span>
      <span class="brand-name">BRIGHTFOLD</span>
      <span class="brand-sub">CHURCH</span>
    </div>

    <p class="contact-name">Dana Cole</p>

    <ul class="contact-list">
      <li>
        <svg class="contact-icon" viewBox="0 0 16 16" aria-hidden="true">
          <circle cx="8" cy="8" r="7" fill="none" stroke="#fff" stroke-width="1.5"/>
          <ellipse cx="8" cy="8" rx="3" ry="7" fill="none" stroke="#fff" stroke-width="1.2"/>
          <line x1="1" y1="8" x2="15" y2="8" stroke="#fff" stroke-width="1.2"/>
        </svg>
        thebrightfoldchurch.com
      </li>
      <li><span class="dot"></span>@ColeDc</li>
      <li><span class="dot"></span>brightfoldchurchfm</li>
    </ul>
  </article>
</div>
</body>
</html>
```